Business Cards and Stationery
Vellomar Development Company
I need single sided standard sized Business Card [3.5" x 2"]
Not sure. Use something compatible with logo.
Professional
Xxxx Xxxxxxx
President
12345 Xxxxxxxxx Xxxxx
Xxxxxxxxx, Xxxxxxxxxx 12345
xxxxxxxxxxx@xxxxxxxxx.xxx
Contractor's License No. 123456
Not that the information will serve as placeholders until the project is awarded and finalized. Actual information will be provided to create final source files.

```html
<!DOCTYPE html>
<html lang="en">
<head>
<meta charset="utf-8">
<title>Vellomar Development Company — Stationery</title>
<link href="https://fonts.googleapis.com/css2?family=Open+Sans:wght@400;600;800&display=swap" rel="stylesheet">
<style>
  :root{
    --navy:#1d2b5e;
    --navy-deep:#141f47;
    --grey:#b9bcc4;
    --grey-light:#e4e6ea;
    --ink:#3a3f4a;
    --paper:#ffffff;
    --stage:#eceae6;
  }
  *{box-sizing:border-box;margin:0;padding:0}
  html,body{width:1200px;height:734px;overflow:hidden}
  body{background:var(--stage);font-family:"Open Sans",Arial,sans-serif;color:var(--ink);position:relative}
  .sheet{position:absolute;background:var(--paper);box-shadow:0 2px 6px rgba(0,0,0,.18);overflow:hidden}
  .swoosh{position:absolute;left:0;bottom:0;width:100%;display:block}
  .brand{display:flex;align-items:center;gap:6px}
  .brand-dot{width:18px;height:18px;border-radius:50%;background:var(--navy);flex:none}
  .brand-name{font-weight:800;color:var(--navy);font-size:15px;letter-spacing:.5px}
  .brand.on-dark .brand-dot{background:#fff}
  .brand.on-dark .brand-name{color:#fff}
  .tiny{font-size:5px;line-height:1.6}
  .watermark{position:absolute;border-radius:50%;background:var(--grey-light);opacity:.7}

  /* business cards */
  .card{width:200px;height:114px}
  .card-front{left:40px;top:40px;background:var(--navy);color:#fff;padding:14px 16px}
  .card-front .person{font-size:8px;font-weight:600}
  .card-front .role{font-size:6px;opacity:.8;margin-bottom:22px}
  .card-front .tiny{color:#dfe3f0}
  .card-back{left:60px;top:168px;padding:30px 20px}
  .card-back .brand-name{font-size:17px}

  /* envelopes */
  .envelope{width:320px;height:150px}
  .envelope-back{left:40px;top:308px}
  .envelope-back .flap{position:absolute;inset:0;width:100%;height:100%}
  .envelope-back .brand{position:absolute;left:134px;top:70px}
  .envelope-front{left:40px;top:474px;height:220px;width:320px}
  .envelope-front .brand{position:absolute;left:18px;top:16px}
  .envelope-front .brand-name{font-size:12px}
  .envelope-front .brand-dot{width:14px;height:14px}

  /* letterhead & fax */
  .page{width:360px;height:466px;top:30px}
  .letterhead{left:400px}
  .fax{left:800px}
  .page-head{position:absolute;left:22px;top:20px;right:22px}
  .contact{display:flex;gap:18px;margin-top:6px}
  .page .watermark{width:90px;height:90px;left:135px;top:300px}
  .fax-title{position:absolute;right:22px;top:62px;font-size:11px;color:var(--navy);font-weight:600;letter-spacing:1px}
  .fax-table{position:absolute;left:22px;right:22px;top:80px;border-collapse:collapse;font-size:5px;width:316px}
  .fax-table td{border:1px solid var(--grey);height:12px;padding:0 4px}
  .fax-table td.label{background:var(--grey-light);width:40px;color:var(--navy);font-weight:600}
  .checks{position:absolute;left:22px;top:154px;display:flex;gap:18px;font-size:5px}
  .checks span::before{content:"";display:inline-block;width:5px;height:5px;border:1px solid var(--grey);margin-right:3px;vertical-align:-1px}
  .fax .body-line{position:absolute;left:22px;top:170px;font-size:5px}

  /* compliment slips */
  .slip{width:360px;height:170px;top:530px}
  .slip-one{left:400px}
  .slip-two{left:800px}
  .slip .page-head{top:18px}
</style>
</head>
<body>

  <!-- business card: details side -->
  <section class="sheet card card-front" aria-label="Business card, details side">
    <p class="person">Xxxx Xxxxxxx</p>
    <p class="role">President</p>
    <p class="tiny">12345 Xxxxxxxxx Xxxxx<br>Xxxxxxxxx, Xxxxxxxxxx 12345<br>xxxxxxxxxxx@xxxxxxxxx.xxx<br>Contractor's License No. 123456</p>
  </section>

  <!-- business card: brand side -->
  <section class="sheet card card-back" aria-label="Business card, brand side">
    <div class="brand"><span class="brand-dot"></span><span class="brand-name">VELLOMAR</span></div>
    <svg class="swoosh" viewBox="0 0 200 24" preserveAspectRatio="none" height="24">
      <path d="M0 14 Q100 2 200 8" fill="none" stroke="var(--grey)" stroke-width="1.5"/>
      <path d="M0 18 Q100 6 200 12 L200 24 L0 24Z" fill="var(--navy)"/>
    </svg>
  </section>

  <!-- envelope back -->
  <section class="sheet envelope envelope-back" aria-label="Envelope, back">
    <svg class="flap" viewBox="0 0 320 150" preserveAspectRatio="none">
      <path d="M0 0 L320 0 L320 40 Q160 100 0 40Z" fill="var(--navy)"/>
      <path d="M0 46 Q160 106 320 46" fill="none" stroke="var(--grey)" stroke-width="1.5"/>
    </svg>
    <div class="brand"><span class="brand-dot"></span><span class="brand-name" style="font-size:11px">VELLOMAR</span></div>
  </section>

  <!-- envelope front -->
  <section class="sheet envelope envelope-front" aria-label="Envelope, front">
    <div class="brand"><span class="brand-dot"></span><span class="brand-name">VELLOMAR</span></div>
    <p class="tiny" style="position:absolute;left:18px;top:36px">12345 Xxxxxxxxx Xxxxx<br>Xxxxxxxxx, Xxxxxxxxxx 12345</p>
    <svg class="swoosh" viewBox="0 0 320 30" preserveAspectRatio="none" height="30">
      <path d="M0 16 Q160 2 320 10" fill="none" stroke="var(--grey)" stroke-width="1.5"/>
      <path d="M0 21 Q160 7 320 15 L320 30 L0 30Z" fill="var(--navy)"/>
    </svg>
  </section>

  <!-- letterhead -->
  <section class="sheet page letterhead" aria-label="Letterhead">
    <div class="page-head">
      <div class="brand"><span class="brand-dot"></span><span class="brand-name">VELLOMAR</span></div>
      <div class="contact tiny">
        <p>12345 Xxxxxxxxx Xxxxx<br>Xxxxxxxxx, Xxxxxxxxxx 12345</p>
        <p><b>Phone:</b> 123 456 7890<br><b>Fax:</b> 123 456 7891<br><b>Email:</b> xxxxxxxxxxx@xxxxxxxxx.xxx</p>
      </div>
    </div>
    <div class="watermark"></div>
    <svg class="swoosh" viewBox="0 0 360 34" preserveAspectRatio="none" height="34">
      <path d="M0 18 Q180 2 360 12" fill="none" stroke="var(--grey)" stroke-width="2"/>
      <path d="M0 24 Q180 8 360 18 L360 34 L0 34Z" fill="var(--navy)"/>
    </svg>
  </section>

  <!-- fax cover -->
  <section class="sheet page fax" aria-label="Fax cover sheet">
    <div class="page-head">
      <div class="brand"><span class="brand-dot"></span><span class="brand-name">VELLOMAR</span></div>
      <div class="contact tiny">
        <p>12345 Xxxxxxxxx Xxxxx<br>Xxxxxxxxx, Xxxxxxxxxx 12345</p>
        <p><b>Phone:</b> 123 456 7890<br><b>Fax:</b> 123 456 7891<br><b>Email:</b> xxxxxxxxxxx@xxxxxxxxx.xxx</p>
      </div>
    </div>
    <p class="fax-title">FAX</p>
    <table class="fax-table">
      <tr><td class="label">To</td><td></td><td class="label">From</td><td></td></tr>
      <tr><td class="label">Fax</td><td></td><td class="label">Pages</td><td></td></tr>
      <tr><td class="label">Phone</td><td></td><td class="label">Date</td><td></td></tr>
      <tr><td class="label">Re</td><td></td><td class="label">CC</td><td></td></tr>
    </table>
    <div class="checks"><span>Urgent</span><span>For Review</span><span>Please Comment</span><span>Please Reply</span><span>Recycle</span></div>
    <p class="body-line">Comments:</p>
    <div class="watermark"></div>
    <svg class="swoosh" viewBox="0 0 360 34" preserveAspectRatio="none" height="34">
      <path d="M0 18 Q180 2 360 12" fill="none" stroke="var(--grey)" stroke-width="2"/>
      <path d="M0 24 Q180 8 360 18 L360 34 L0 34Z" fill="var(--navy)"/>
    </svg>
  </section>

  <!-- compliment slips -->
  <section class="sheet slip slip-one" aria-label="Compliment slip">
    <div class="page-head">
      <div class="brand"><span class="brand-dot"></span><span class="brand-name">VELLOMAR</span></div>
      <p class="tiny" style="margin-top:6px">12345 Xxxxxxxxx Xxxxx<br>Xxxxxxxxx, Xxxxxxxxxx 12345</p>
    </div>
    <svg class="swoosh" viewBox="0 0 360 30" preserveAspectRatio="none" height="30">
      <path d="M0 16 Q180 2 360 10" fill="none" stroke="var(--grey)" stroke-width="2"/>
      <path d="M0 21 Q180 7 360 15 L360 30 L0 30Z" fill="var(--navy)"/>
    </svg>
  </section>

  <section class="sheet slip slip-two" aria-label="Compliment slip">
    <div class="page-head">
      <div class="brand"><span class="brand-dot"></span><span class="brand-name">VELLOMAR</span></div>
      <p class="tiny" style="margin-top:6px">12345 Xxxxxxxxx Xxxxx<br>Xxxxxxxxx, Xxxxxxxxxx 12345</p>
    </div>
    <svg class="swoosh" viewBox="0 0 360 30" preserveAspectRatio="none" height="30">
      <path d="M0 16 Q180 2 360 10" fill="none" stroke="var(--grey)" stroke-width="2"/>
      <path d="M0 21 Q180 7 360 15 L360 30 L0 30Z" fill="var(--navy)"/>
    </svg>
  </section>

</body>
</html>
```